Brightpath Orthodontics business card design

Need a business card design that reflects our re-branding (orthodontic office - braces) and a new partnership with a pediatric dental office. We would like to include "for adults and children" on the card as well so adults know they are welcome to get their braces here as well. Office design is modern and would like business card to reflect a modern type look. Here's the text we would like to be included on the card:

Darren Holloway, DDS, MSD
5214 West Maple Avenue, Suite 204
Mansfield, TX 76099
817-555-0143
www.brightpathortho.example
info@brightpathortho.example
Updates

Can we add the following to the existing designs? Darren Holloway, DDS, MSD 5214 West Maple Avenue, Suite 204 Mansfield, TX 76099 817-555-0143

Does anyone have any more vertical designs available? Thanks!

Industry/Entity Type

Dental

```html
<!DOCTYPE html>
<html lang="en">
<head>
<meta charset="utf-8">
<title>Brightpath Orthodontics – Business Card</title>
<link href="https://fonts.googleapis.com/css2?family=Exo+2:wght@500;600;700&display=swap" rel="stylesheet">
<style>
  :root {
    --page-bg: #e9e9e7;
    --card-white: #ffffff;
    --brand-blue: #1277c0;
    --accent-warm: #f4a45a;
    --accent-mid: #ee6aa8;
    --accent-cool: #a8d36f;
    --ink: #1a1a1a;
    --on-blue: #ffffff;
  }
  html, body {
    margin: 0;
    width: 1200px;
    height: 900px;
    overflow: hidden;
    background: var(--page-bg);
    font-family: "Exo 2", sans-serif;
  }
  .card {
    position: absolute;
    left: 100px;
    top: 164px;
    width: 1000px;
    height: 572px;
    background: var(--card-white);
    box-shadow: 0 6px 24px rgba(0,0,0,0.18);
    overflow: hidden;
  }
  .card-panel {
    position: absolute;
    inset: 0;
    width: 1000px;
    height: 572px;
  }
  .accent-band {
    position: absolute;
    inset: 0;
    width: 1000px;
    height: 572px;
  }
  .tagline {
    position: absolute;
    right: 40px;
    top: 36px;
    margin: 0;
    font-size: 20px;
    font-weight: 600;
    color: var(--ink);
  }
  .brand {
    position: absolute;
    left: 60px;
    top: 92px;
    display: flex;
    align-items: center;
    gap: 18px;
  }
  .brand-dot {
    width: 64px;
    height: 64px;
    border-radius: 50%;
    background: var(--brand-blue);
    flex: none;
  }
  .brand-name {
    margin: 0;
    font-size: 46px;
    font-weight: 700;
    line-height: 1.02;
    color: var(--ink);
  }
  .address {
    position: absolute;
    right: 40px;
    top: 212px;
    margin: 0;
    text-align: right;
    font-style: normal;
    font-size: 22px;
    font-weight: 500;
    line-height: 32px;
    color: var(--on-blue);
  }
  .contact-list {
    position: absolute;
    right: 40px;
    top: 340px;
    margin: 0;
    padding: 0;
    list-style: none;
    text-align: right;
    font-size: 22px;
    font-weight: 500;
    line-height: 34px;
    color: var(--on-blue);
  }
  .contact-list li {
    display: flex;
    justify-content: flex-end;
    align-items: center;
    gap: 10px;
  }
  .contact-icon {
    width: 20px;
    height: 20px;
    flex: none;
  }
  .doctor {
    position: absolute;
    left: 110px;
    top: 440px;
    color: var(--on-blue);
  }
  .doctor-name {
    margin: 0;
    font-size: 32px;
    font-weight: 600;
    line-height: 38px;
  }
  .doctor-credentials {
    margin: 0;
    font-size: 22px;
    font-weight: 600;
    line-height: 30px;
  }
</style>
</head>
<body>
  <section class="card">
    <svg class="accent-band" viewBox="0 0 1000 572" role="img" aria-label="Decorative colour swoosh artwork area">
      <defs>
        <linearGradient id="accentFade" x1="0" y1="0" x2="1" y2="0">
          <stop offset="0" stop-color="var(--accent-warm)"/>
          <stop offset="0.5" stop-color="var(--accent-mid)"/>
          <stop offset="1" stop-color="var(--accent-cool)"/>
        </linearGradient>
      </defs>
      <path fill="url(#accentFade)" d="M0,270 C300,260 600,150 1000,90 L1000,130 C700,150 400,330 0,352 Z"/>
    </svg>
    <svg class="card-panel" viewBox="0 0 1000 572" aria-hidden="true">
      <path fill="var(--brand-blue)" d="M0,352 C400,330 700,150 1000,130 L1000,572 L0,572 Z"/>
    </svg>

    <p class="tagline">For Adults and Children</p>

    <div class="brand">
      <span class="brand-dot"></span>
      <h1 class="brand-name">Brightpath<br>Orthodontics</h1>
    </div>

    <address class="address">
      5214 West Maple Avenue,<br>
      Suite 204 Mansfield,<br>
      TX 76099
    </address>

    <ul class="contact-list">
      <li>817-555-0143
        <svg class="contact-icon" viewBox="0 0 20 20" aria-hidden="true"><rect x="5" y="1.5" width="10" height="17" rx="2" fill="none" stroke="currentColor" stroke-width="1.6"/><line x1="8.5" y1="15.5" x2="11.5" y2="15.5" stroke="currentColor" stroke-width="1.6"/></svg>
      </li>
      <li>info@brightpathortho.example
        <svg class="contact-icon" viewBox="0 0 20 20" aria-hidden="true"><rect x="1.5" y="4.5" width="17" height="11" fill="none" stroke="currentColor" stroke-width="1.6"/><path d="M1.5,4.5 L10,11 L18.5,4.5" fill="none" stroke="currentColor" stroke-width="1.6"/></svg>
      </li>
      <li>www.brightpathortho.example
        <svg class="contact-icon" viewBox="0 0 20 20" aria-hidden="true"><circle cx="10" cy="10" r="8.5" fill="none" stroke="currentColor" stroke-width="1.6"/><ellipse cx="10" cy="10" rx="3.5" ry="8.5" fill="none" stroke="currentColor" stroke-width="1.4"/><line x1="1.5" y1="10" x2="18.5" y2="10" stroke="currentColor" stroke-width="1.4"/></svg>
      </li>
    </ul>

    <div class="doctor">
      <p class="doctor-name">Darren Holloway</p>
      <p class="doctor-credentials">DDS, MSD</p>
    </div>
  </section>
</body>
</html>
```